Legal Journal cover - modern and sylish

We require a cover design for a new, modern and digital legal academic journal. Attached is our logo so you can get an idea of the feel. This academic journal will have several editions per year.Requirements for the cover design:-The feel of the cover is to be modern -In harmony with our logo-While staying uniform and set in its design,
Updates

Colors
ec1f27

Requirements
Must have
• 1) Colour. Each edition will use different colours. (So we will need the source files to be able to continue to do this)
• 2) An image section. We would like to be able to put in different image or photo with each edition. So we need to have a section, most likely in the shape of a strip, that can include a different image or photo each edition. This part is where we can put a different image in for each edition. So this section would need to be able to accommodate different types of images. It could be a single square. Or it could be a line (a strip) that an image or images.
• 3) A title for the edition and volume and number. Like this:
• Volume 34, No 2 (2016): Contemporary Issues in Criminal Law
• I have attached a range of journals I found online to serve as inspiration.

```html
<!DOCTYPE html>
<html lang="en">
<head>
<meta charset="utf-8">
<title>Journal Cover</title>
<link rel="stylesheet" href="https://fonts.googleapis.com/css2?family=Arimo:wght@400&family=Poppins:wght@700&display=swap">
<style>
  :root {
    --page: #ffffff;
    --slate: #72706d;
    --signal-red: #d9251d;
    --image-fill: #dfdfdd;
    --ink: #222222;
    --white: #ffffff;
  }
  html, body {
    margin: 0;
    padding: 0;
    width: 1200px;
    height: 1200px;
    overflow: hidden;
    background: var(--page);
  }
  .canvas {
    display: block;
    width: 1200px;
    height: 1200px;
  }
  .cover-top { fill: var(--slate); }
  .cover-bottom { fill: var(--signal-red); }
  .image-frame-arc {
    fill: none;
    stroke: var(--white);
    stroke-width: 38;
    stroke-linecap: butt;
  }
  .image-slot { fill: var(--image-fill); }
  .image-label {
    font-family: "Arimo", Arial, sans-serif;
    font-size: 34px;
    fill: var(--ink);
  }
  .brand-ring { fill: var(--slate); }
  .brand-disc, .brand-band { fill: var(--white); }
  .brand-dot { fill: var(--signal-red); }
  .brand-name {
    font-family: "Poppins", Arial, sans-serif;
    font-weight: 700;
    font-size: 82px;
    fill: var(--signal-red);
    letter-spacing: 2px;
  }
</style>
</head>
<body>
<svg class="canvas" viewBox="0 0 1932 1932" xmlns="http://www.w3.org/2000/svg">
  <g class="cover">
    <rect class="cover-top" x="502" y="299" width="928" height="1333"/>
    <path class="cover-bottom"
          d="M502,1085 C530,900 570,850 620,820 L1290,570 C1370,505 1415,410 1430,299 L1430,1632 L502,1632 Z"/>
  </g>

  <g class="feature-image">
    <path class="image-frame-arc" d="M1309,729 A343,343 0 1 0 877,1060"/>
    <circle class="image-slot" cx="966" cy="729" r="307" role="img" aria-label="Edition feature image"/>
    <text class="image-label" x="966" y="740" text-anchor="middle">Image Section</text>
  </g>

  <g class="masthead">
    <circle class="brand-ring" cx="870" cy="1347" r="212"/>
    <rect class="brand-band" x="1000" y="1231" width="430" height="232"/>
    <circle class="brand-disc" cx="870" cy="1347" r="195"/>
    <circle class="brand-dot" cx="870" cy="1347" r="70"/>
    <text class="brand-name" x="1000" y="1328">JURIS</text>
    <text class="brand-name" x="1000" y="1420">LENS</text>
  </g>
</svg>
</body>
</html>
```